Bright Mesh Business Card

This is a business card for a printing company but I actually don't have a logo. Just need to typeset the words "Bright Mesh Printing" as the logo. Then add my name "Loretta Vance" + phone number + address

Target Market(s)

ceos and professionals

Industry/Entity Type

printing and manufacturing

Contact Information for Business Card

Bright Mesh Printing/ 4617 calloway st. S. El Monte, CA 91648/ 626-417-3980/ Loretta Vance

Font styles to use
Serif
Other font styles liked:
• a modern font would be nice

Colors
0054AA
0677BA
7BADD7
CADEEF
E8F1F8
0094D4
00A9DD
6FCCEA
C7EBF8
E9F6FB

Requirements
Must have
• company name, number, address
Nice to have
• nice bold feel
Should not have
• nothing in particular

```html
<!DOCTYPE html>
<html lang="en">
<head>
<meta charset="utf-8">
<title>Bright Mesh Printing – Business Card</title>
<link href="https://fonts.googleapis.com/css2?family=Montserrat:wght@500;700;800&family=Source+Serif+4:wght@400&display=swap" rel="stylesheet">
<style>
  :root {
    --backdrop: #c9c9c9;
    --charcoal: #2a2c2d;
    --charcoal-soft: #3d3f40;
    --brand-blue: #0054aa;
    --bright-blue: #2a72c9;
    --sky: #6fccea;
    --paper: #ffffff;
    --ink: #2a2c2d;
  }
  * { margin: 0; padding: 0; box-sizing: border-box; }
  html, body { width: 1200px; height: 988px; overflow: hidden; }
  body { background: var(--backdrop); position: relative; font-family: "Montserrat", sans-serif; }

  .card {
    position: absolute;
    width: 540px;
    height: 310px;
    border-radius: 18px;
    overflow: hidden;
    box-shadow: 0 6px 18px rgba(0,0,0,.25);
  }

  /* Front */
  .card-front { left: 50px; top: 120px; background: var(--charcoal); }
  .front-texture {
    position: absolute; inset: 0;
    background: linear-gradient(150deg, var(--charcoal-soft) 0%, var(--charcoal) 35%, #4a4c4d 55%, var(--charcoal) 72%);
  }
  .wordmark {
    position: absolute;
    left: 0; right: 0; top: 112px;
    display: flex; align-items: center; justify-content: center; gap: 14px;
  }
  .wordmark-square { width: 34px; height: 34px; flex: none; }
  .wordmark-text { font-weight: 700; line-height: 1; white-space: nowrap; }
  .wordmark-name { font-size: 36px; letter-spacing: .5px; display: block; }
  .wordmark-sub { font-size: 19px; letter-spacing: 13px; display: block; margin-top: 8px; }
  .card-front .wordmark-text { color: var(--bright-blue); }
  .card-front .wordmark-square { background: var(--bright-blue); }

  /* Back */
  .card-back { left: 610px; top: 560px; background: var(--paper); }
  .back-waves { position: absolute; inset: 0; width: 100%; height: 100%; }
  .card-back .wordmark { left: 30px; right: auto; top: 138px; justify-content: flex-start; gap: 12px; }
  .card-back .wordmark-text { color: var(--brand-blue); }
  .card-back .wordmark-square { background: var(--brand-blue); width: 30px; height: 30px; }
  .card-back .wordmark-name { font-size: 26px; }
  .card-back .wordmark-sub { font-size: 14px; letter-spacing: 10px; margin-top: 6px; }

  .holder { position: absolute; right: 36px; top: 22px; text-align: right; }
  .holder-name { font-weight: 800; font-size: 30px; color: var(--brand-blue); line-height: 1; }
  .holder-title { font-weight: 500; font-size: 14px; color: var(--ink); margin-top: 4px; letter-spacing: .5px; }

  .contact {
    position: absolute; right: 14px; top: 170px;
    font-family: "Source Serif 4", serif; font-size: 12px; color: var(--paper);
    text-align: right; line-height: 1.5; list-style: none;
  }
  .contact li { display: flex; justify-content: flex-end; align-items: center; gap: 6px; white-space: nowrap; }
  .contact svg { width: 11px; height: 11px; flex: none; }
  .icon-spacer { width: 11px; display: inline-block; flex: none; }
</style>
</head>
<body>

<section class="card card-front" aria-label="Business card front">
  <div class="front-texture" role="img" aria-label="Dark ink-splatter texture band across the card"></div>
  <div class="wordmark">
    <span class="wordmark-square"></span>
    <span class="wordmark-text">
      <span class="wordmark-name">BRIGHT MESH</span>
      <span class="wordmark-sub">PRINTING</span>
    </span>
  </div>
</section>

<section class="card card-back" aria-label="Business card back">
  <svg class="back-waves" viewBox="0 0 540 310" preserveAspectRatio="none" aria-hidden="true">
    <path d="M540,94 C420,99 330,124 300,184 C270,244 240,298 170,310 L540,310 Z" fill="var(--charcoal)"/>
    <path d="M540,80 C414,86 318,114 288,178 C258,242 226,296 150,310 L165,310 C232,298 262,244 293,182 C324,120 416,92 540,88 Z" fill="var(--brand-blue)"/>
    <path d="M282,190 C252,250 218,298 130,310 L145,310 C228,300 258,254 287,196 Z" fill="var(--sky)"/>
    <rect x="526" y="28" width="14" height="44" fill="var(--brand-blue)"/>
  </svg>

  <div class="holder">
    <div class="holder-name">Loretta Vance</div>
    <div class="holder-title">Directeur printing</div>
  </div>

  <div class="wordmark">
    <span class="wordmark-square"></span>
    <span class="wordmark-text">
      <span class="wordmark-name">BRIGHT MESH</span>
      <span class="wordmark-sub">PRINTING</span>
    </span>
  </div>

  <ul class="contact">
    <li>4617 calloway st. S. El Monte,<span class="icon-spacer"></span></li>
    <li>CA 91648/ 626-417-3980/ Loretta Vance<span class="icon-spacer"></span></li>
    <li>+123 456 7890
      <svg viewBox="0 0 12 12"><circle cx="6" cy="6" r="6" fill="var(--sky)"/><path d="M4 3.2l1 1.6-.6.7c.4.8 1 1.4 1.8 1.8l.7-.6 1.6 1-.5 1.1C6 8.6 3.4 6 3 4z" fill="var(--charcoal)"/></svg>
    </li>
    <li>info@youremail.com
      <svg viewBox="0 0 12 12"><rect x="1" y="2.5" width="10" height="7" fill="var(--sky)"/><path d="M1 2.5l5 4 5-4" stroke="var(--charcoal)" fill="none"/></svg>
    </li>
    <li>www.yourwebsite.com
      <svg viewBox="0 0 12 12"><circle cx="6" cy="6" r="5.5" fill="var(--sky)"/><path d="M.5 6h11M6 .5c-2 2.5-2 8.5 0 11M6 .5c2 2.5 2 8.5 0 11" stroke="var(--charcoal)" stroke-width=".8" fill="none"/></svg>
    </li>
  </ul>
</section>

</body>
</html>
```